Digitales Briefpapier für IT-Systemhaus
Zielgruppe
IT-Systemhaus mit dem Schwerpunkt Digitalisierung von Geschäftsprozessen. Ggf. Schlagwörter wie DMS, ECM, Digitalisierung Ihrer Prozesse unterbringen.
Aufgabenstellung
Digitale Vorlage (Word) um daraus dann ein PDF zu generieren. Anschrift usw. auf QXN.de

```html
<!DOCTYPE html>
<html lang="de">
<head>
<meta charset="utf-8">
<title>QXN.de Briefpapier</title>
<link href="https://fonts.googleapis.com/css2?family=Open+Sans:wght@300;400;600&display=swap" rel="stylesheet">
<style>
  :root {
    --navy: #253859;
    --blue: #3d6db5;
    --text: #444a52;
    --line: #5a5f66;
    --paper: #ffffff;
  }
  * { margin: 0; padding: 0; box-sizing: border-box; }
  html, body { width: 847px; height: 1200px; overflow: hidden; background: var(--paper); }
  body { font-family: "Open Sans", Arial, sans-serif; color: var(--text); }
  .letterhead { position: relative; width: 847px; height: 1200px; background: var(--paper); }

  .header-band { position: absolute; left: 0; top: 0; width: 100%; height: 115px; background: var(--navy); }
  .brand-name { position: absolute; left: 78px; top: 22px; font-size: 50px; font-weight: 300; color: var(--blue); letter-spacing: 3px; line-height: 1; }
  .tagline { position: absolute; right: 34px; top: 52px; font-size: 14px; font-weight: 400; color: var(--blue); }

  .address-window { position: absolute; left: 78px; top: 159px; width: 351px; height: 170px; }
  .address-window svg { position: absolute; inset: 0; }
  .sender-line { position: absolute; left: 45px; top: 20px; font-size: 7px; white-space: nowrap; border-bottom: 0.8px solid var(--line); padding-bottom: 1px; }
  .sender-line .company { color: var(--blue); }
  .sender-line .sep { color: #999; margin: 0 4px; }

  .contact-block { position: absolute; left: 633px; top: 159px; font-size: 10px; line-height: 15.5px; }
  .contact-block .company { color: var(--blue); font-weight: 600; }
  .contact-block .label { color: var(--blue); font-weight: 600; margin-right: 4px; }
  .contact-block .group { margin-top: 5px; }
  .contact-block .legal { margin-top: 8px; }

  .fold-mark { position: absolute; left: 29px; width: 5px; height: 9px; }
  .fold-mark.first { top: 446px; }
  .fold-mark.second { top: 759px; }

  .footer-band { position: absolute; left: 0; bottom: 0; width: 100%; height: 21px; background: var(--navy); }
</style>
</head>
<body>
<div class="letterhead">
  <header class="header-band">
    <div class="brand-name">QXN.de</div>
    <div class="tagline">DMS, ECM, Digitalisierung Ihrer Prozesse unterbringen.</div>
  </header>

  <div class="address-window">
    <svg width="351" height="170" viewBox="0 0 351 170" fill="none" stroke="var(--line)" stroke-width="0.9">
      <path d="M0.5 30 V14 A13 13 0 0 1 13.5 1 H29"/>
      <path d="M322 1 H337.5 A13 13 0 0 1 350.5 14 V30"/>
      <path d="M0.5 140 V156 A13 13 0 0 0 13.5 169 H29"/>
      <path d="M322 169 H337.5 A13 13 0 0 0 350.5 156 V140"/>
    </svg>
    <div class="sender-line"><span class="company">QXN.de Systemhaus GmbH &amp; Co. KG</span><span class="sep">|</span>Talstraße 14a<span class="sep">|</span>30159 Hannover</div>
  </div>

  <address class="contact-block" style="font-style: normal;">
    <div class="company">QXN.de Systemhaus GmbH &amp; Co. KG</div>
    <div>Talstraße 14a</div>
    <div>30159 Hannover</div>
    <div class="group">
      <div><span class="label">T.</span>+49 (511) 4870120</div>
      <div><span class="label">F.</span>+49 (511) 48701299</div>
      <div><span class="label">E.</span>info(at)qxn.de</div>
      <div><span class="label">W.</span>www.qxn.de</div>
    </div>
    <div class="legal">
      <div>Amtsgericht Hannover</div>
      <div>IBAN DE12 3456 7890 0123 4567 89</div>
      <div>BIC QXNBDE22XXX</div>
      <div>Ust. ID: DE123456789</div>
    </div>
  </address>

  <svg class="fold-mark first" viewBox="0 0 5 9"><path d="M0 0 L5 4.5 L0 9 Z" fill="var(--blue)"/></svg>
  <svg class="fold-mark second" viewBox="0 0 5 9"><path d="M0 0 L5 4.5 L0 9 Z" fill="var(--blue)"/></svg>

  <footer class="footer-band"></footer>
</div>
</body>
</html>
```